Property investment company needs a letterhead design!

We are a new residential and commercial property investment company. Name of the company is Morvesta Group, LLC. We have a new logo and now we need letterhead! We prefer to have a professional and upscale appearance. We don't have any fixed requirements, so be creative! Thank you for considering this project. We are so excited to see what happens!

Target Market(s)

Professional

Industry/Entity Type

Real Estate Development

```html
<!DOCTYPE html>
<html lang="en">
<head>
<meta charset="utf-8">
<title>Morvesta Group, LLC — Letterhead</title>
<link rel="stylesheet" href="https://fonts.googleapis.com/css2?family=Montserrat:wght@400;700&display=swap">
<style>
  :root {
    --navy: #06203f;
    --sky-band: #b3e5f8;
    --bright-blue: #00aeef;
    --paper: #ffffff;
    --faint: #e6e7eb;
  }
  * { margin: 0; padding: 0; box-sizing: border-box; }
  html, body { width: 848px; height: 1200px; overflow: hidden; background: var(--paper); }
  .letterhead {
    position: relative;
    width: 848px;
    height: 1200px;
    background: var(--paper);
    font-family: "Montserrat", sans-serif;
    color: var(--navy);
  }
  .brand-mark {
    position: absolute;
    left: 25px;
    top: 62px;
    display: flex;
    align-items: center;
    gap: 8px;
  }
  .brand-mark .dot {
    width: 14px; height: 14px; border-radius: 50%;
    background: var(--navy);
  }
  .brand-mark .name {
    font-weight: 700;
    font-size: 19px;
    letter-spacing: 0.5px;
    color: var(--navy);
    line-height: 1.1;
  }
  .brand-watermark {
    position: absolute;
    left: 0; right: 0;
    top: 570px;
    text-align: center;
    font-weight: 700;
    font-size: 52px;
    letter-spacing: 1px;
    color: var(--faint);
    line-height: 1.2;
  }
  .footer-band {
    position: absolute;
    left: 0; top: 1092px;
    width: 848px; height: 89px;
    background: var(--sky-band);
  }
  .contact-row {
    position: absolute;
    left: 25px; top: 1125px;
    display: flex;
    align-items: center;
    font-size: 14px;
    color: var(--navy);
    white-space: nowrap;
  }
  .contact-item { display: flex; align-items: center; }
  .contact-item svg { flex: none; }
  .contact-item.address svg { margin-right: 10px; }
  .contact-item.phone { margin-left: 8px; }
  .contact-item.phone svg { margin-right: 10px; }
  .contact-item.email { margin-left: 6px; }
  .contact-item.email svg { margin-right: 6px; }
  .contact-item.web { margin-left: 11px; }
  .contact-item.web svg { margin-right: 9px; }
  .footer-brand {
    position: absolute;
    right: 8px; top: 1160px;
    font-weight: 700;
    font-size: 11px;
    color: var(--navy);
  }
  .base-bar-dark {
    position: absolute;
    left: 0; top: 1181px;
    width: 669px; height: 19px;
    background: var(--navy);
  }
  .base-bar-bright {
    position: absolute;
    left: 669px; top: 1181px;
    width: 179px; height: 19px;
    background: var(--bright-blue);
  }
</style>
</head>
<body>
<main class="letterhead">
  <header class="brand-mark">
    <span class="dot"></span>
    <span class="name">Morvesta Group, LLC</span>
  </header>

  <div class="brand-watermark" aria-hidden="true">Morvesta Group, LLC</div>

  <footer>
    <div class="footer-band"></div>
    <div class="contact-row">
      <div class="contact-item address">
        <svg width="18" height="24" viewBox="0 0 18 24" aria-hidden="true">
          <path d="M9 1C4.6 1 1.2 4.4 1.2 8.7 1.2 14 9 23 9 23s7.8-9 7.8-14.3C16.8 4.4 13.4 1 9 1z" fill="none" stroke="var(--navy)" stroke-width="1.6"/>
          <circle cx="9" cy="8.6" r="3" fill="none" stroke="var(--navy)" stroke-width="1.6"/>
        </svg>
        <span>123, Your Address Here</span>
      </div>
      <div class="contact-item phone">
        <svg width="21" height="21" viewBox="0 0 24 24" aria-hidden="true">
          <path d="M6.6 2.2l2.6 3.6c.4.6.3 1.3-.2 1.8L7.4 9.1c1.4 3 3.9 5.6 7 7.1l1.5-1.6c.5-.5 1.2-.6 1.8-.2l3.6 2.5c.6.4.8 1.2.4 1.9l-1.4 2.4c-.5.8-1.5 1.2-2.4.9C10.5 19.9 4.2 13.6 2 6.2c-.3-.9.1-1.9.9-2.4l1.9-1.3c.6-.4 1.4-.3 1.8.2z" fill="var(--navy)"/>
        </svg>
        <span>Phone No. : +123456789</span>
      </div>
      <div class="contact-item email">
        <svg width="21" height="14" viewBox="0 0 21 14" aria-hidden="true">
          <rect x="0" y="0" width="21" height="14" fill="var(--navy)"/>
          <path d="M1.5 1.5l9 6.5 9-6.5M1.5 12.5l6.5-5M19.5 12.5l-6.5-5" fill="none" stroke="var(--sky-band)" stroke-width="1.1"/>
        </svg>
        <span>emal@emailid.com</span>
      </div>
      <div class="contact-item web">
        <svg width="16" height="22" viewBox="0 0 16 22" aria-hidden="true">
          <path d="M1 1v16l4-3.5 3 7 2.6-1.1-3-6.8H14z" fill="var(--navy)"/>
        </svg>
        <span>www.website.com</span>
      </div>
    </div>
    <div class="footer-brand">Morvesta Group, LLC</div>
    <div class="base-bar-dark"></div>
    <div class="base-bar-bright"></div>
  </footer>
</main>
</body>
</html>
```